Website for International Non-Profit for Birth Parent Searching

Tovira is a 501(c)(3) non-profit organization that helps Chinese adoptees search and reunite with birth families who were separated due the One Child Policy in China. We want to create a website that can link to an information database that allows website users to easily access information around search ads in an organized way; help connect families to professional searchers; provide resources for community support for adoptees and their families as they embark on a personal and emotional journey of finding birth family through support groups on social media and consultation/education on the searching process; and provide the opportunity for the adoptive community to give back through donations and volunteer opportunities. The final design should foster a sense of community and be easy navigable to access the multiple resources we provide to help families search for each other. We would like to see designs with red/black/white color schemes that are gentle, inviting, and family friendly to viewers. We would like to see some design layouts with Chinese themes, if possible.

```html
<!DOCTYPE html>
<html lang="en">
<head>
<meta charset="utf-8">
<title>Tovira – Donations</title>
<link href="https://fonts.googleapis.com/css2?family=Lato:wght@700;900&family=Fira+Sans:wght@400;500;600&family=Roboto:wght@400;500&display=swap" rel="stylesheet">
<style>
  :root {
    --red: #9b0510;
    --red-bright: #d31f26;
    --ink: #1a1a1a;
    --text: #2b2b2b;
    --white: #ffffff;
    --panel: #f1f1f1;
    --panel-light: #fafafa;
    --line: #dedede;
    --footer: #0c0c0c;
    --hero-navy: #2a3656;
    --hero-rose: #9c5e66;
    --hero-skin: #b98478;
  }
  * { margin: 0; padding: 0; box-sizing: border-box; }
  html, body { width: 925px; height: 1200px; overflow: hidden; background: var(--white); }
  body { position: relative; font-family: "Fira Sans", sans-serif; color: var(--text); }

  .site-header { position: absolute; top: 0; left: 0; width: 925px; height: 69px; background: var(--white); z-index: 3; }
  .brand-tab { position: absolute; left: 49px; top: -10px; width: 142px; height: 142px; border-radius: 50%; background: var(--white); z-index: 4; display: flex; align-items: flex-end; justify-content: center; padding-bottom: 30px; }
  .brand-name { font-family: "Lato", sans-serif; font-weight: 900; font-size: 25px; color: var(--red-bright); }
  .main-nav { position: absolute; top: 0; left: 0; height: 69px; width: 925px; font-family: "Lato", sans-serif; font-weight: 700; font-size: 12px; color: var(--ink); }
  .main-nav span { position: absolute; top: 26px; white-space: nowrap; }
  .chev { position: absolute; top: 30px; }
  .btn-donate { position: absolute; left: 713px; top: 16px; width: 115px; height: 31px; background: var(--red); color: var(--white); border-radius: 2px; display: flex; align-items: center; justify-content: center; font-family: "Lato", sans-serif; font-weight: 700; font-size: 11px; }

  .hero { position: absolute; top: 69px; left: 0; width: 925px; height: 300px;
    background: linear-gradient(90deg, var(--hero-navy) 0%, var(--hero-rose) 30%, var(--hero-skin) 50%, var(--hero-rose) 70%, var(--hero-navy) 100%); }
  .hero-wave { position: absolute; top: 0; left: 0; z-index: 2; }
  .hero-actions { position: absolute; top: 202px; left: 304px; display: flex; gap: 14px; z-index: 2; }
  .hero-btn { width: 151px; height: 38px; display: flex; align-items: center; justify-content: center; font-family: "Lato", sans-serif; font-weight: 700; font-size: 11px; border-radius: 2px; }
  .hero-btn.solid { background: var(--white); color: var(--ink); }
  .hero-btn.outline { border: 1.5px solid var(--white); color: var(--white); }

  .section-title { position: absolute; left: 0; width: 925px; text-align: center; font-family: "Lato", sans-serif; font-weight: 900; font-size: 27px; color: var(--ink); letter-spacing: -0.3px; }
  .section-text { position: absolute; left: 150px; width: 625px; text-align: center; font-size: 15px; line-height: 24px; color: var(--text); }

  .donate-form { position: absolute; left: 111px; top: 557px; width: 703px; height: 185px; border: 1px solid var(--line); background: var(--panel-light); }
  .amount-row { height: 84px; background: var(--panel); position: relative; }
  .amount-label { position: absolute; left: 155px; top: 36px; font-weight: 600; font-size: 11px; color: var(--ink); }
  .amount-select { position: absolute; left: 218px; top: 25px; width: 311px; height: 35px; background: var(--white); border: 1px solid #bdbdbd; border-radius: 3px; font-size: 11px; padding: 0 14px; display: flex; align-items: center; justify-content: space-between; color: var(--ink); }
  .frequency { position: absolute; top: 116px; left: 0; }
  .freq-btn { position: absolute; top: 0; height: 34px; background: var(--red); color: var(--white); border-radius: 2px; display: flex; align-items: center; justify-content: center; font-family: "Roboto", sans-serif; font-weight: 500; font-size: 11px; letter-spacing: 0.5px; }

  .site-footer { position: absolute; top: 963px; left: 0; width: 925px; height: 237px; background: var(--footer); color: var(--white); font-family: "Roboto", sans-serif; }
  .footer-brand { position: absolute; left: 118px; top: 123px; width: 120px; text-align: center; font-family: "Lato", sans-serif; font-weight: 900; font-size: 27px; color: var(--white); }
  .footer-nav span { position: absolute; top: 54px; font-weight: 500; font-size: 10px; }
  .footer-rule { position: absolute; left: 281px; top: 85px; width: 522px; height: 1px; background: #d8d8d8; }
  .contact { position: absolute; top: 106px; display: flex; gap: 11px; font-size: 10.5px; line-height: 14px; }
  .contact-icon { width: 22px; height: 22px; background: var(--white); display: flex; align-items: center; justify-content: center; margin-top: 1px; flex-shrink: 0; }
  .copyright { position: absolute; left: 281px; top: 160px; font-size: 8px; letter-spacing: 0.2px; }
</style>
</head>
<body>

<header class="site-header">
  <nav class="main-nav">
    <span style="left:234px">HOME</span>
    <span style="left:290px">WHO WE ARE</span>
    <svg class="chev" style="left:372px" width="8" height="6" viewBox="0 0 8 6"><path d="M1 1l3 3 3-3" fill="none" stroke="#1a1a1a" stroke-width="1.4"/></svg>
    <span style="left:391px">START YOUR SEARCH</span>
    <span style="left:525px">GET INVOLVED</span>
    <span style="left:625px">RESOURCES</span>
    <a class="btn-donate">DONATE NOW</a>
    <span style="left:844px">EN</span>
    <svg class="chev" style="left:866px" width="8" height="6" viewBox="0 0 8 6"><path d="M1 1l3 3 3-3" fill="none" stroke="#1a1a1a" stroke-width="1.4"/></svg>
  </nav>
</header>
<div class="brand-tab"><span class="brand-name">Tovira</span></div>

<section class="hero" role="img" aria-label="Photo of two pairs of cupped hands holding a small red heart"></section>
<svg class="hero-wave" width="925" height="370" viewBox="0 0 925 370">
  <path d="M0,336 C150,300 300,305 460,335 S800,352 925,283 L925,370 L0,370 Z" fill="#9b0510"/>
  <path d="M0,352 C150,316 300,318 460,346 S800,370 925,290 L925,370 L0,370 Z" fill="#ffffff"/>
</svg>
<div class="hero-actions">
  <a class="hero-btn solid">CREATE AN ACCOUNT</a>
  <a class="hero-btn outline">LOGIN</a>
</div>

<h1 class="section-title" style="top:421px">DONATIONS</h1>
<p class="section-text" style="top:471px">Donations go directly to funding the day-to-day operations of the organization so we can continue to provide the services and care to the birth parent search community.</p>

<form class="donate-form">
  <div class="amount-row">
    <span class="amount-label">Other</span>
    <div class="amount-select">$0.00
      <svg width="8" height="6" viewBox="0 0 8 6"><path d="M1 1l3 3 3-3" fill="none" stroke="#1a1a1a" stroke-width="1.3"/></svg>
    </div>
  </div>
  <div class="frequency">
    <a class="freq-btn" style="left:29px;width:189px">ONE-TIME DONATION</a>
    <a class="freq-btn" style="left:224px;width:124px">WEEKLY</a>
    <a class="freq-btn" style="left:355px;width:153px">MONTHLY</a>
    <a class="freq-btn" style="left:515px;width:159px">ANNUAL DONATION</a>
  </div>
</form>

<h2 class="section-title" style="top:784px">DONATE A DNA KIT</h2>
<p class="section-text" style="top:835px;left:157px;width:600px">Each DNA kit donated will go to a birth family to submit their DNA in our centralized DNA database to increase the odds of Chinese birth families and Chinese adoptees to find each other.</p>

<footer class="site-footer">
  <div class="footer-brand">Tovira</div>
  <nav class="footer-nav">
    <span style="left:281px">HOME</span>
    <span style="left:331px">WHO WE ARE</span>
    <span style="left:415px">OUR SERVICES</span>
    <span style="left:508px">GET INVOLVED</span>
    <span style="left:598px">TOOLS AND RESOURCES</span>
    <span style="left:737px">CONTACT US</span>
  </nav>
  <div class="footer-rule"></div>
  <div class="contact" style="left:281px">
    <span class="contact-icon"><svg width="12" height="12" viewBox="0 0 24 24"><path d="M6.6 10.8a15 15 0 006.6 6.6l2.2-2.2c.3-.3.7-.4 1-.2 1.1.4 2.3.6 3.6.6.6 0 1 .4 1 1V20c0 .6-.4 1-1 1A17 17 0 013 4c0-.6.4-1 1-1h3.5c.6 0 1 .4 1 1 0 1.3.2 2.5.6 3.6.1.3 0 .7-.2 1z" fill="#9b0510"/></svg></span>
    <div>Phone:<br>555-014-2297</div>
  </div>
  <div class="contact" style="left:411px">
    <span class="contact-icon"><svg width="12" height="12" viewBox="0 0 24 24"><path d="M12 2a7 7 0 00-7 7c0 5 7 13 7 13s7-8 7-13a7 7 0 00-7-7zm0 9.5A2.5 2.5 0 1112 6.5a2.5 2.5 0 010 5z" fill="#9b0510"/></svg></span>
    <div>2810 W Juniper Ridge Way,<br>4B, Lakeview, CO 80123</div>
  </div>
  <div class="contact" style="left:604px">
    <span class="contact-icon"><svg width="12" height="12" viewBox="0 0 24 24"><path d="M2 5h20v14H2z" fill="#9b0510"/><path d="M2 6l10 7 10-7" fill="none" stroke="#fff" stroke-width="1.8"/></svg></span>
    <div>Email:<br>hello@toviracharities.org</div>
  </div>
  <div class="copyright">© COPYRIGHTS 2021 TOVIRA &nbsp;| &nbsp; ALL RIGHTS RESERVED</div>
</footer>

</body>
</html>
```